I need a business card that is professional /minimalistic ( clean edges) to help develop my new business venture that is car valeting / detailing.

I would like to use a black background, white font,red car silhouette above the text.

have now added phone numbers thanks

Industry/Entity Type

Business

Contact Information for Business Card

Gleamcraft Studio,
Valeting & Detailing Specialist,
tel 01638 219054 mob 07814 605193, Dean Marlowe, 7 Hawthorn Rise. East Brackley, Marshford. IP19 3JD

```html
<!DOCTYPE html>
<html lang="en">
<head>
<meta charset="utf-8">
<title>Gleamcraft Studio – Business Card</title>
<link rel="stylesheet" href="https://fonts.googleapis.com/css2?family=Russo+One&display=swap">
<style>
  :root {
    --stage: #2a2a2a;
    --card: #141414;
    --red: #e0262b;
    --white: #f2f2f2;
    --grey: #c9c9c9;
  }
  html, body {
    margin: 0;
    width: 1200px;
    height: 900px;
    overflow: hidden;
    background: var(--stage);
  }
  .business-card {
    position: absolute;
    left: 100px;
    top: 160px;
    width: 1000px;
    height: 580px;
    background: var(--card);
    font-family: "Russo One", sans-serif;
    text-transform: uppercase;
    overflow: hidden;
  }
  .car-silhouette {
    position: absolute;
    left: 40px;
    top: 150px;
    width: 920px;
    height: 380px;
    border-radius: 190px 240px 40px 40px;
    background: radial-gradient(ellipse at 55% 45%, rgba(224, 38, 43, 0.32), rgba(224, 38, 43, 0.08) 70%, rgba(224, 38, 43, 0) 100%);
  }
  .contact {
    position: absolute;
    right: 60px;
    top: 50px;
    text-align: right;
  }
  .contact__name {
    margin: 0;
    color: var(--red);
    font-size: 34px;
    letter-spacing: 1px;
  }
  .contact__address {
    margin: 10px 0 0;
    color: var(--white);
    font-size: 15px;
    letter-spacing: 1px;
  }
  .contact__phones {
    margin: 28px 0 0;
    font-size: 30px;
    line-height: 1.3;
  }
  .contact__label { color: var(--red); }
  .contact__number { color: var(--white); }
  .brand {
    position: absolute;
    left: 330px;
    top: 360px;
  }
  .brand__name {
    margin: 0;
    color: var(--red);
    font-size: 46px;
    letter-spacing: 1px;
  }
  .brand__tagline {
    margin: 6px 0 0;
    color: var(--grey);
    font-size: 20px;
    letter-spacing: 1.5px;
  }
</style>
</head>
<body>
  <main class="business-card">
    <div class="car-silhouette" role="img" aria-label="Red outline silhouette of a sports car"></div>

    <section class="contact">
      <h1 class="contact__name">Dean Marlowe</h1>
      <p class="contact__address">7 Hawthorn Rise. East Brackley. Marshford. IP19 3JD</p>
      <p class="contact__phones">
        <span class="contact__label">Tel</span> <span class="contact__number">01638 219054</span><br>
        <span class="contact__label">Mob</span> <span class="contact__number">07814 605193</span>
      </p>
    </section>

    <section class="brand">
      <h2 class="brand__name">Gleamcraft Studio</h2>
      <p class="brand__tagline">Valeting &amp; Detailing Specialist</p>
    </section>
  </main>
</body>
</html>
```